Commercial LED Lighting Company need Product Catalog

We need a product catalog for our commercial LED Lighting company. We sell indoor and outdoor lighting fixtures to commercial customers, for commercial purposes. Most of our clients are knowledgeable about our products, and are interested in the technical details of our products.

Our catalog will offer 17 products, with a two page layout for each product. We have a specific vision for the general outline of the product layout. Attached, you will see a competitor's design whose layout we'd like to mimic - the first page for a product will have a large photo up top of a room or space showcasing the product, and the bottom half will be a photo of the product with some general bullet points. The second page will list the various model numbers for the products, along with their technical details. All information needed for the project will be provided, including product photos. We will not include all product photos in our attachment today, as we are limited to how many files we can upload at this time. Also attached is a general outline of the catalog, as well as product details.

Our clients are professionals, and we want to communicate a respect for our clients' know how and industry experience. We also want to maintain our color palate of blue, white and grey. I will also attach our logo to give you a reference.

Sample designs should include a potential cover design, and a two page layout for a single product.

Target Market(s)

LED Lighting Distributors; engineers; professional customers

Industry/Entity Type

Manufacturer

Font styles to use
Sans Serif

Colors
0355a3
cfdeed
85acd3
3276b5
eaf1f7

Requirements
Must have
• All required technical information as outlined in attached documents; all 17 products; the two page layout we have envisioned; our color scheme.

```html
<!DOCTYPE html>
<html lang="en">
<head>
<meta charset="utf-8">
<title>Beadline Transitional Style – Catalog Spread</title>
<link href="https://fonts.googleapis.com/css2?family=Josefin+Sans:wght@400;600;700&family=Montserrat:wght@500;600&display=swap" rel="stylesheet">
<style>
  :root{
    --navy:#0355a3;
    --mid-blue:#3276b5;
    --sky:#85acd3;
    --pale:#cfdeed;
    --mist:#eaf1f7;
    --ink:#1b1b1b;
    --rule:#9db8db;
    --white:#ffffff;
  }
  *{box-sizing:border-box;margin:0;padding:0}
  html,body{width:1200px;height:777px;overflow:hidden;background:var(--white)}
  body{font-family:"Josefin Sans",sans-serif;color:var(--ink);position:relative}
  .abs{position:absolute}

  .band{position:absolute;left:0;width:1200px}
  .band-top{top:0;height:28px;background:var(--mist)}
  .band-bottom{top:758px;height:19px;background:var(--mist)}

  .section-label{left:39px;top:9px;font-family:"Montserrat",sans-serif;font-weight:600;font-size:12.5px;letter-spacing:.2px;color:var(--ink)}

  .hero-photo{left:0;top:28px;width:600px;height:365px;
    background:linear-gradient(180deg,#d9d6d0 0%,#a9a397 45%,#5b5650 75%,#3e3f44 100%)}
  .title-band{left:0;top:393px;width:600px;height:53px;background:var(--pale);padding:5px 0 0 22px}
  .title-band h1{font-size:22px;font-weight:700;line-height:1.15;color:var(--ink)}
  .title-band p{font-size:15px;line-height:1.15;color:var(--ink)}

  .feature{left:31px;top:484px;width:232px;font-size:9.6px;line-height:13px}
  .feature h2{font-size:9.8px;font-weight:700;margin-bottom:1px}
  .feature p{text-align:justify;margin-bottom:12px}

  .product-small{left:298px;top:496px;width:254px;height:128px;border-radius:50% / 45%;
    background:radial-gradient(ellipse at 50% 60%,#ffffff 0%,#ececec 55%,#9a9a9a 80%,#cfcfcf 100%)}
  .product-large{left:724px;top:312px;width:332px;height:176px;border-radius:50% / 45%;
    background:radial-gradient(ellipse at 50% 62%,#ffffff 0%,#ededed 55%,#979797 80%,#d2d2d2 100%)}

  .spec-head{left:644px;top:43px}
  .spec-head h2{font-size:14.5px;font-weight:400;letter-spacing:.2px}
  .spec-head .size{margin-top:3px;font-size:9.6px;display:flex;gap:27px;font-family:"Montserrat",sans-serif;font-weight:500}
  .spec-head .size span:last-child{color:#2a5fd6;font-weight:400}

  .badges{left:968px;top:44px;display:flex;gap:20px;align-items:flex-start}
  .badge-label{font-family:"Montserrat",sans-serif;font-weight:600;font-size:8.5px;text-align:center;margin-top:2px}

  table{border-collapse:collapse}
  .tech{left:970px;top:109px;width:205px;font-size:8.6px}
  .tech caption{text-align:left;font-weight:700;font-size:9px;padding:0 0 3px 10px}
  .tech td{height:16.8px;border-top:1.5px solid var(--rule);padding:3px 0 0 10px}
  .tech tr:last-child td{border-bottom:1.5px solid var(--rule)}
  .tech td+td{border-left:1.5px solid var(--rule);text-align:center;padding-left:0;width:92px}

  .models{left:626px;top:614px;width:530px;font-size:8.6px}
  .models th{font-family:"Montserrat",sans-serif;font-weight:600;font-size:8.8px;height:19px;text-align:left;padding:3px 0 0 17px;border-top:1.5px solid var(--rule)}
  .models th+th,.models td+td{border-left:1.5px solid var(--rule)}
  .models td{height:17.6px;border-top:1.5px solid var(--rule);padding:3px 0 0 17px}
  .models tr:last-child td{border-bottom:1.5px solid var(--rule)}
  .models td:nth-child(n+2){text-align:center;padding-left:0}

  .folio{top:762px;font-size:8.5px}
</style>
</head>
<body>
  <div class="band band-top"></div>
  <svg class="abs" style="left:0;top:0" width="1200" height="28" aria-hidden="true">
    <polygon points="312,0 890,0 870,28 334,28" fill="var(--sky)"/>
  </svg>
  <div class="abs section-label">OUTDOOR FIXTURES</div>

  <div class="abs hero-photo" role="img" aria-label="Executive office interior with desk, lounge chairs and sofa, lit by the ceiling fixture"></div>
  <div class="abs title-band">
    <h1>Beadline Transitional Style</h1>
    <p>Flush Mount LED Ceiling Light</p>
  </div>

  <div class="abs feature">
    <h2>Feature</h2>
    <p>Veloran Beadline Transitional Style Flush Mount LED Ceiling Light is designed with a beautifully brushed-nickel double-ring finish to blend in with all of your décor. It's available in three sizes to fit for your different room design. Compatible with a variety of dimmer switches, the fixture can be mounted on either a ceiling or wall to provide light anywhere you need it. Also, choosing this energy-efficient LED lighting solution over incandescent will save you money on operating costs and you never have to change another bulb.</p>
    <h2>Specifications</h2>
    <div>Material: Acrylic Diffuser + Aluminum Base</div>
    <div>Finish: Nickle</div>
    <div>Beam Angle: 120°</div>
    <div>Input Voltage: AC120V</div>
    <div>Warranty: 8 Years</div>
  </div>

  <div class="abs product-small" role="img" aria-label="Angled view of the brushed-nickel double-ring flush mount fixture"></div>

  <div class="abs spec-head">
    <h2>Beadline Transitional Style Flush Mount LED</h2>
    <div class="size"><span>SIZE</span><span>12in x 3.35 in</span></div>
  </div>

  <div class="abs badges">
    <svg width="56" height="44" aria-hidden="true"><circle cx="28" cy="22" r="18" fill="none" stroke="var(--ink)" stroke-width="3"/></svg>
    <svg width="32" height="32" aria-hidden="true"><rect width="32" height="32" fill="var(--mid-blue)"/></svg>
    <div>
      <svg width="24" height="24" aria-hidden="true"><circle cx="12" cy="11" r="9" fill="none" stroke="var(--ink)" stroke-width="2.4"/><path d="M8 15 L16 7" stroke="var(--ink)" stroke-width="2.4"/><path d="M9 8 q3 -1 4 2 q1 3 -3 4" fill="none" stroke="var(--ink)" stroke-width="1.6"/></svg>
      <div class="badge-label">DRY</div>
    </div>
    <div>
      <svg width="50" height="24" aria-hidden="true"><path d="M6 22 A19 19 0 0 1 44 22" fill="none" stroke="var(--ink)" stroke-width="4"/><text x="9" y="22" font-size="8" font-family="Montserrat,sans-serif">-</text><text x="35" y="22" font-size="8" font-family="Montserrat,sans-serif">+</text></svg>
      <div class="badge-label">DIMMABLE</div>
    </div>
  </div>

  <table class="abs tech">
    <caption>Technical Data</caption>
    <tr><td>CRI</td><td>&gt;80</td></tr>
    <tr><td>Beam Angle</td><td>140°</td></tr>
    <tr><td>Operation Temp.</td><td>-30° ~ 60°</td></tr>
    <tr><td>Lifespan</td><td>50,000 Hours</td></tr>
    <tr><td>Waterproof Rating</td><td>Wet Location</td></tr>
    <tr><td>Lumen per watt</td><td>&gt; 90 lm/w</td></tr>
  </table>

  <div class="abs product-large" role="img" aria-label="Front view of the brushed-nickel double-ring flush mount fixture with white acrylic diffuser"></div>

  <table class="abs models">
    <tr><th>MODEL NUMBER</th><th>WATTAGE</th><th>COLOR TEMP</th><th>LUMENS</th><th>DIAMETER (INCH)</th></tr>
    <tr><td>LED-BDLT12N15W3K</td><td>15 Watts</td><td>3000K</td><td>1050 Lm</td><td>12"</td></tr>
    <tr><td>LED-BDLT12N15W4K</td><td>15 Watts</td><td>4000K</td><td>1050 Lm</td><td>12"</td></tr>
    <tr><td>LED-BDLT14N20W3K</td><td>20 Watts</td><td>3000K</td><td>1400 Lm</td><td>14"</td></tr>
    <tr><td>LED-BDLT14N20W4K</td><td>20 Watts</td><td>4000K</td><td>1400 Lm</td><td>14"</td></tr>
    <tr><td>LED-BDLT18N28W3K</td><td>28 Watts</td><td>3000K</td><td>2000 Lm</td><td>18"</td></tr>
    <tr><td>LED-BDLT18N28W4K</td><td>28 Watts</td><td>4000K</td><td>2000 Lm</td><td>18"</td></tr>
  </table>

  <div class="band band-bottom"></div>
  <svg class="abs" style="left:0;top:758px" width="1200" height="19" aria-hidden="true">
    <polygon points="84,0 1120,0 1104,19 100,19" fill="var(--sky)"/>
  </svg>
  <div class="abs folio" style="left:39px">2</div>
  <div class="abs folio" style="left:1160px">3</div>
</body>
</html>
```